Property Portal needs Chatterbook Cover Image and Sponsor Ad Design

WHO WE ARE
Hi Pitchers! We are an advertising portal that focus on presenting the latest property launches in Singapore. Our platform and interface will provide consumer an enjoyable and easy browsing experience looking for their ideal property to buy/invest, while ensuring updated information, images/videos, and other useful description is provided on each project.

WHAT WE NEED
Our website is www.brightkeyhomes.sg, and we need designs for our Chatterbook page www.facebook.com/brightkeyhomes. One as the Cover Image (815 x 315), and one as our Sponsor Ad Image (1200 x 627). The 2 designs can be similar or different.

DESIGN
We want to convey a professional and sociable feel. A "cool" and elegant design may be suitable, although feel free to have your own look & feel as long as it suits our purpose. Try to have a focus, and not look messy. We don't want to look cheap, spammy or boring in any sense. Be creative and purposeful =) You may use the snapvault images attached or you can use your own. Add symbols or graphics if it helps to give the design a better feel.

For your reference, I find there is a number of good designs with nice look & feel in this project including those withdraw/eliminated.
http://social.pitchhive.com/contest.aspx?id=718206&page=2
http://social.pitchhive.com/contest.aspx?id=718206

IDEAS
You may want to embed our portal in an SLATEPAD device as part of the design (see samples below but replace slatephone with SlatePad). And/or you can have a blur-out image background to have a focus on what you want to show. Please note that we are not restricting any other designs concept, this is just an idea I have.

CAPTIONS
You may use one or a few of the sample captions below.
- Singapore Latest Property Launches In One Portal (slight emphasis on "in one portal")
- Latest Projects • Updated Info • Best Pricing
- Residential • Commercial • Overseas (perhaps label on images)

Hope we can find an ideal design here. We will request from pitchhive to increase the project budget to give out more participation payments if there is a few good ones. We are also looking to find suitable designers for our future projects as we need a few more designs. If you have questions, feel free to ask me and I will reply promptly.
Updates

Reason: Project cancelled and relaunch with different purpose, moved from Newsletter to Chatterbook Design.

IDEAS (UPDATED) I am thinking one way to showcase our portal is perhaps to have our website embedded in an slatepad and/or pebblebook device as part of the design. I've attached some designs I came across to show what I mean (only the embedding part). If you are going to do it this way, you can use our main page www.brightkeyhomes.sg and/or a project page www.brightkeyhomes.sg/lakeshade-at-morrowdale to display

Target Market(s)

Real Estate Agents, Investors, Developers, General public age 30 & above

Industry/Entity Type

Advertising

Colors
9ccb3b
00a98f
0592cd
3176b5
ffcf3e
5c5c5c

Requirements
Should not have
• I prefer not to use real people stock images unless you are very sure it will work out well.

```html
<!DOCTYPE html>
<html lang="en">
<head>
<meta charset="utf-8">
<title>Brightkeyhomes – Singapore Latest Property Launches</title>
<link rel="stylesheet" href="https://fonts.googleapis.com/css2?family=Oswald:wght@400;500&family=Open+Sans:wght@400;600;700&family=Lora:wght@400&display=swap">
<style>
  :root {
    --sky-top: #2a2c4e;
    --sky-mid: #6b5a8a;
    --sky-low: #b58aa6;
    --tower-dark: #2b2522;
    --tower-glow: #8a5a2c;
    --pool: #1d3a5a;
    --hand-tone: #c9a08a;
    --device-dark: #1b1b1d;
    --band: rgba(20, 20, 24, 0.72);
    --white: #ffffff;
    --green: #8cc63f;
    --brand-green: #3a9a3e;
    --text-dark: #3a3a3a;
    --text-mid: #5c5c5c;
    --rule: #d8d8d8;
  }
  * { box-sizing: border-box; margin: 0; padding: 0; }
  html, body { width: 1200px; height: 627px; overflow: hidden; background: #222; }
  .ad {
    position: relative;
    width: 1200px;
    height: 627px;
    overflow: hidden;
    font-family: "Open Sans", sans-serif;
  }
  .scene-photo {
    position: absolute; inset: 0;
    background:
      radial-gradient(ellipse at 88% 20%, var(--sky-low) 0%, transparent 45%),
      linear-gradient(90deg, var(--tower-dark) 0%, var(--tower-glow) 30%, #6b4a3a 52%, var(--sky-mid) 72%, var(--sky-top) 100%);
  }
  .scene-photo::after {
    content: ""; position: absolute; left: 0; right: 0; bottom: 0; height: 190px;
    background: linear-gradient(180deg, rgba(29,58,90,0) 0%, var(--pool) 55%, #12263d 100%);
  }
  .hand-photo {
    position: absolute; left: 100px; top: 88px; width: 460px; height: 539px;
    border-radius: 60px 60px 0 0;
    background: linear-gradient(160deg, var(--device-dark) 0%, #2c2c30 45%, var(--hand-tone) 80%, #a87d66 100%);
  }
  .screen {
    position: absolute; left: 246px; top: 172px; width: 240px; height: 322px;
    background: var(--white);
    border-radius: 3px;
    overflow: hidden;
    transform: rotate(-2deg);
    transform-origin: center;
  }
  .status-bar {
    height: 12px; background: #111; color: var(--white);
    font-size: 8px; line-height: 12px; text-align: center; font-weight: 600;
  }
  .site-header { padding: 6px 12px 5px; border-bottom: 2px solid var(--brand-green); margin: 0 8px; }
  .brand { display: flex; align-items: center; gap: 5px; }
  .brand-dot { width: 14px; height: 14px; border-radius: 50%; background: var(--brand-green); }
  .brand-name { font-family: "Open Sans", sans-serif; font-weight: 700; font-size: 16px; color: var(--brand-green); letter-spacing: -0.3px; }
  .brand-tagline { font-size: 4.5px; color: var(--text-mid); letter-spacing: 0.4px; margin-left: 19px; }
  .listing-photo {
    position: relative; margin: 8px 12px 0; height: 88px;
    background: linear-gradient(180deg, #4a5a78 0%, #8a6a52 55%, #2d4f6e 100%);
  }
  .price-tag {
    position: absolute; left: 50%; bottom: -9px; transform: translateX(-50%);
    background: var(--green); color: var(--white);
    font-size: 9px; font-weight: 700; padding: 3px 12px; border-radius: 10px;
    border: 2px solid var(--white);
  }
  .listing-title {
    font-family: "Lora", serif; font-size: 15px; color: var(--text-dark);
    text-align: center; margin-top: 16px; padding-bottom: 5px;
    border-bottom: 1px solid var(--rule); margin-left: 14px; margin-right: 14px;
  }
  .facts { list-style: none; padding: 5px 16px 0; }
  .facts li { display: flex; align-items: center; gap: 6px; font-size: 6.5px; color: var(--text-dark); line-height: 13px; }
  .facts svg { width: 7px; height: 7px; fill: var(--text-mid); flex: none; }
  .view-button {
    display: block; margin: 8px auto 0; width: 90px; text-align: center;
    font-size: 6.5px; font-weight: 700; color: var(--text-dark);
    border: 1px solid var(--rule); border-radius: 10px; padding: 4px 0;
    box-shadow: 0 1px 2px rgba(0,0,0,0.15);
  }
  .headline-band {
    position: absolute; left: 668px; top: 344px; width: 532px; height: 113px;
    background: var(--band);
  }
  .headline {
    position: absolute; left: 686px; top: 356px;
    font-family: "Oswald", sans-serif; font-weight: 400; color: var(--white);
    line-height: 1.12;
  }
  .headline-top { display: block; font-size: 33px; }
  .headline-bottom { display: block; font-size: 33px; }
  .headline-accent { color: var(--green); font-size: 42px; font-weight: 500; }
</style>
</head>
<body>
<main class="ad">
  <div class="scene-photo" role="img" aria-label="Dusk view of lit condominium towers beside a pool with fountains and palm trees"></div>
  <div class="hand-photo" role="img" aria-label="Hand holding a smartphone showing the property portal"></div>

  <section class="screen" aria-label="Portal listing on phone">
    <div class="status-bar">5:05 PM</div>
    <header class="site-header">
      <div class="brand"><span class="brand-dot"></span><span class="brand-name">brightkeyhomes.sg</span></div>
      <div class="brand-tagline">FIND THE LATEST PROPERTY LAUNCHES TODAY</div>
    </header>
    <div class="listing-photo" role="img" aria-label="Condominium towers with fountain pool">
      <span class="price-tag">$760,000++</span>
    </div>
    <h2 class="listing-title">Linden Springs</h2>
    <ul class="facts">
      <li><svg viewBox="0 0 10 10"><path d="M5 1 L9.5 5 H8 V9 H2 V5 H0.5 Z"/></svg>Executive Condominium • 99 years</li>
      <li><svg viewBox="0 0 10 10"><path d="M5 0.5 A3.2 3.2 0 0 1 8.2 3.7 C8.2 6 5 9.5 5 9.5 C5 9.5 1.8 6 1.8 3.7 A3.2 3.2 0 0 1 5 0.5 Z"/></svg>Woodlands (D25)</li>
      <li><svg viewBox="0 0 10 10"><rect x="1" y="1.5" width="8" height="2"/><rect x="1" y="4.5" width="8" height="2"/><rect x="1" y="7.5" width="8" height="2"/></svg>418 units • 2BR to 4BR</li>
      <li><svg viewBox="0 0 10 10"><rect x="2" y="0.5" width="6" height="9"/></svg>TOP 2016 • by Harbourline Estates</li>
      <li><svg viewBox="0 0 10 10"><circle cx="5" cy="5" r="4.5"/></svg>$7xxpsf</li>
    </ul>
    <span class="view-button">VIEW THIS PROJECT</span>
  </section>

  <div class="headline-band"></div>
  <h1 class="headline">
    <span class="headline-top">Singapore Latest Property</span>
    <span class="headline-bottom">Launches <span class="headline-accent">In One Portal</span></span>
  </h1>
</main>
</body>
</html>
```